Responsive webpage design for an exsiting layout (romain catholic church)

Example of content and layout on: [url removed, login to view]

header: "Pastoralraum Birkenhal Ost" and the banners (attachement)
The mainmenu entires will be "Pastoralraum", "Talwiken", "Mooswil", "Grenzbach", "Lindenwerd", "Waldersil", "Zweckverband".
however new entries may follow.
The submenus are different (like on example page)

We need:
- new design (should not look like the other page)
- responsive design
- the colors and design should be matching for a romain catholic church (liturgical colors)
- the page should be "light" (not too much dark colors, background...)

```html
<!DOCTYPE html>
<html lang="de">
<head>
<meta charset="utf-8">
<title>Römisch Katholische Kirchgemeinde Birkenhal</title>
<link href="https://fonts.googleapis.com/css2?family=Cabin:wght@400;500;600&family=Arimo:wght@400;700&display=swap" rel="stylesheet">
<style>
:root{
  --brown:#8a4b35;
  --nav-bg:#f1ede8;
  --nav-ink:#3a3a3a;
  --ink:#1a1a1a;
  --grey-text:#7a7a7a;
  --line:#d6d6d6;
  --panel:#ffffff;
  --btn:#f4f4f4;
}
*{box-sizing:border-box;margin:0;padding:0}
html,body{width:1200px;height:735px;overflow:hidden;background:#fff}
body{position:relative;font-family:"Cabin",sans-serif;color:var(--ink)}
.abs{position:absolute}

.brand{left:17px;top:10px;font-family:"Arimo",sans-serif;font-weight:700;font-size:19px;line-height:22.5px;color:var(--ink);text-transform:uppercase}

.search-divider{left:890px;top:12px;width:1px;height:68px;background:#e2e2e2}
.search-label{left:924px;top:13px;font-size:17px;color:#555}
.search-field{left:924px;top:44px;width:236px;height:38px;border:1px solid #bdbdbd;border-right:none;background:#fff}
.search-btn{left:1160px;top:44px;width:36px;height:38px;background:var(--brown);display:flex;align-items:center;justify-content:center}

.main-nav{left:9px;top:111px;width:1187px;height:60px;background:var(--nav-bg);border-top:1px solid #e0d9d1;border-bottom:4px solid var(--brown);display:flex}
.main-nav a{color:var(--nav-ink);text-decoration:none;font-size:17px;display:flex;align-items:center;padding:0 21px;height:55px;white-space:nowrap}
.main-nav a.active{background:var(--brown);color:#fff;padding:0 22px 0 18px}

.stage{left:9px;top:177px;width:1187px;height:416px;border:1px solid var(--line);background:var(--panel)}
.hero{left:20px;top:187px;width:803px;height:396px;background:linear-gradient(180deg,#a7a29b 0%,#8b7d70 35%,#5b4233 70%,#3b2a20 100%)}
.hero-caption{left:20px;top:473px;width:803px;height:110px;background:rgba(25,25,25,.82);padding:20px 24px 0}
.hero-caption h2{font-weight:400;font-size:20px;color:#fff;margin-bottom:4px}
.hero-caption p{font-family:"Arimo",sans-serif;font-size:12px;line-height:20px;color:#eee}
.arrow{width:50px;height:50px}

.welcome{left:833px;top:187px;width:350px;height:396px;border:1px solid var(--line);background:#fff}
.welcome-head{left:833px;top:187px;width:350px;height:51px;background:var(--brown);color:#fff;font-size:20px;padding:13px 14px}
.welcome-photo{left:848px;top:253px;width:321px;height:146px;background:linear-gradient(90deg,#2e2e2e,#8c8c8c 45%,#d8d8d8 75%,#9a9a9a)}
.welcome-text{left:848px;top:418px;width:321px;font-family:"Arimo",sans-serif;font-size:12px;line-height:21px;color:var(--grey-text)}
.quick-links{left:848px;top:520px;width:321px;height:44px;border:1px solid #d2d2d2;border-radius:3px;display:flex;background:var(--btn);box-shadow:0 1px 2px rgba(0,0,0,.12)}
.quick-links span{flex:1;display:flex;align-items:center;justify-content:center;gap:6px;font-family:"Arimo",sans-serif;font-size:12px;color:#333;border-right:1px solid #d2d2d2}
.quick-links span:last-child{border-right:none}

.rule{left:0;top:617px;width:1200px;height:2px;background:#d0d0d0}

.notice{left:9px;top:644px;width:1187px;height:76px;border:1px solid #dcdcdc;background:#fff}
.notice-tag{left:13px;top:649px;width:175px;height:66px}
.notice-tag-label{left:37px;top:668px;color:#fff;font-size:19px}
.notice-title{left:208px;top:656px;color:var(--brown);font-size:20px}
.notice-sub{left:208px;top:684px;font-family:"Arimo",sans-serif;font-size:12px;color:#666}
.notice-btn{top:659px;height:45px;border:1px solid #c9c9c9;border-radius:3px;background:var(--btn);display:flex;align-items:center;justify-content:center;gap:8px;font-size:17px;color:#333}
.notice-close{left:1157px;top:672px;width:20px;height:20px}
</style>
</head>
<body>

<div class="abs brand">Römisch<br>Katholische<br>Kirchgemeinde<br>Birkenhal</div>

<div class="abs search-divider"></div>
<div class="abs search-label">Search Now</div>
<div class="abs search-field"></div>
<div class="abs search-btn">
  <svg width="16" height="16" viewBox="0 0 16 16"><circle cx="6.5" cy="6.5" r="4.5" fill="none" stroke="#fff" stroke-width="2"/><line x1="10" y1="10" x2="14" y2="14" stroke="#fff" stroke-width="2.5" stroke-linecap="round"/></svg>
</div>

<nav class="abs main-nav">
  <a class="active" href="#">Pastoralraum</a>
  <a href="#">Talwiken</a>
  <a href="#">Mooswil</a>
  <a href="#">Grenzbach</a>
  <a href="#">Lindenwerd</a>
  <a href="#">Waldersil</a>
  <a href="#">Zweckverband</a>
</nav>

<div class="abs stage"></div>
<div class="abs hero" role="img" aria-label="Photograph of a red-brick Gothic church with spires under a cloudy sky"></div>
<svg class="abs arrow" style="left:35px;top:358px" viewBox="0 0 50 50"><circle cx="25" cy="25" r="23" fill="#6a6a6a" stroke="#cfcfcf" stroke-width="3"/><circle cx="25" cy="25" r="16" fill="none" stroke="#fff" stroke-width="2.5"/><path d="M31 25H18M23 19l-6 6 6 6" fill="none" stroke="#fff" stroke-width="3" stroke-linecap="round" stroke-linejoin="round"/></svg>
<svg class="abs arrow" style="left:758px;top:358px" viewBox="0 0 50 50"><circle cx="25" cy="25" r="23" fill="#6a6a6a" stroke="#cfcfcf" stroke-width="3"/><circle cx="25" cy="25" r="16" fill="none" stroke="#fff" stroke-width="2.5"/><path d="M19 25h13M27 19l6 6-6 6" fill="none" stroke="#fff" stroke-width="3" stroke-linecap="round" stroke-linejoin="round"/></svg>
<div class="abs hero-caption">
  <h2>Herzlich willkommen...</h2>
  <p>...in den Pfarreien St. Josef | St. Martin | St. Anna | St. Nikolaus des zukunftigen Pastoralraums Birkenhal Ost und in<br>der röm.-kath. Kirchgemeinde Birkenhal</p>
</div>

<div class="abs welcome"></div>
<div class="abs welcome-head">Herzlich willkommen...</div>
<div class="abs welcome-photo" role="img" aria-label="Black and white photograph of a congregation in prayer"></div>
<p class="abs welcome-text">...in den Pfarreien St. Josef | St. Martin | St. Anna | St. Nikolaus des zukunftigen Pastoralraums Birkenhal Ost und in der röm.-kath. Kirchgemeinde Birkenhal</p>
<div class="abs quick-links">
  <span><svg width="11" height="12" viewBox="0 0 11 12"><circle cx="5.5" cy="3" r="3" fill="#333"/><path d="M0 12c0-4 2.5-5.5 5.5-5.5S11 8 11 12z" fill="#333"/></svg>Join Us</span>
  <span><svg width="9" height="13" viewBox="0 0 9 13"><rect x="2.5" y="0" width="4" height="8" rx="2" fill="#333"/><path d="M1 6a3.5 3.5 0 0 0 7 0M4.5 9.5V13M2 13h5" fill="none" stroke="#333" stroke-width="1.2"/></svg>Sermons</span>
  <span><svg width="12" height="11" viewBox="0 0 12 11"><path d="M6 11L1 6A3 3 0 0 1 6 2a3 3 0 0 1 5 4z" fill="#333"/></svg>Support</span>
</div>

<div class="abs rule"></div>

<div class="abs notice"></div>
<svg class="abs notice-tag" viewBox="0 0 175 66"><path d="M0 0H160L175 33L160 66H0Z" fill="#333"/></svg>
<div class="abs notice-tag-label">Notifications</div>
<div class="abs notice-title">Latest Sormens</div>
<div class="abs notice-sub">Lindenhof Schule Baccalaureate, June 6, 6:00 PM</div>
<div class="abs notice-btn" style="left:879px;width:110px">
  <svg width="14" height="14" viewBox="0 0 14 14"><path d="M2 10V7a5 5 0 0 1 10 0v3" fill="none" stroke="#333" stroke-width="1.6"/><rect x="1" y="8.5" width="3" height="5" rx="1" fill="#333"/><rect x="10" y="8.5" width="3" height="5" rx="1" fill="#333"/></svg>Listen</div>
<div class="abs notice-btn" style="left:1001px;width:146px">
  <svg width="14" height="14" viewBox="0 0 14 14"><path d="M7 1v8M3.5 6L7 9.5 10.5 6" fill="none" stroke="#333" stroke-width="1.8"/><path d="M1 10v3h12v-3" fill="none" stroke="#333" stroke-width="1.6"/></svg>Download</div>
<svg class="abs notice-close" viewBox="0 0 20 20"><circle cx="10" cy="10" r="10" fill="#666"/><path d="M6.5 6.5l7 7M13.5 6.5l-7 7" stroke="#fff" stroke-width="2" stroke-linecap="round"/></svg>

</body>
</html>
```